Urgent * Legal Consultant Website Design

Provide a brief overview about your business Hello, website design required for independent legal consultant. Upload your company logo in the brief UPLOADED Specify the main navigation menu of your website (For better reference here's a sample of a website's navigation menu: (http://pixelrow.com/wp-content/uploads/2012/css-menu/ 3.jpg) Header menu should include: About Us, Our people, Services and Contact Us Indicate the subpages or the dropdown menu if you have any (Refer to: http://venmi.co/wp-content/uploads/2010 /11/nav.jpg) No Subpages in the dropdown Upload to separate file for the text or the content needed for the homepage (This is a helpful supporting file to provide in order for our designers to better understand the elements needed on how to layout your This could be in Word document if you're using Windows or in Pages if you are using Mac. ) GET your legal advice and protect you and your BUSINESS Family Law Debt Recovery Leases Crimes & Traffic, wills Violence Restraining Orders Probate Titles Shariah Law Provide some samples of Web designs you like for better reference (Cite 2 to 3 samples) Website must be clean , simple and display our services in a clear way. Examples: https://cdn.plinthora.com/wp/wp-content/uploads/sites/2/brisova-simple-business-wordpress-theme-1024x846.jpg https://cdn.plinthora.com/wp/wp -content / uploads / sites / 2 / corvelle-creative-studio-wp-website-template-1024x791.jpg Upload photos or files you would like to include in the design, or make mention if you are open to use stock photos Open to Use stock photos
Number of Pages Required
1 page

```html
<!DOCTYPE html>
<html lang="en">
<head>
<meta charset="utf-8">
<title>Legal Haven — Independent Legal Consultant</title>
<link href="https://fonts.googleapis.com/css2?family=Roboto:wght@300;400;500;700;900&family=Libre+Baskerville:wght@400;700&display=swap" rel="stylesheet">
<style>
:root{
  --ink:#111111;
  --text:#555555;
  --muted:#8a8a8a;
  --gold:#e9c65b;
  --paper:#ffffff;
  --mist:#f3f3f3;
  --line:#d9d9d9;
  --bar:#333333;
  --serif:'Libre Baskerville', Georgia, serif;
  --sans:'Roboto', Arial, sans-serif;
}
*{box-sizing:border-box;margin:0;padding:0}
html,body{width:1200px;height:4306px;overflow:hidden;background:var(--paper)}
body{font-family:var(--sans);color:var(--ink);position:relative}
.abs{position:absolute}
section,header,footer{position:absolute;left:0;width:1200px}

/* header */
.site-header{top:0;height:135px;background:var(--paper)}
.brand{left:75px;top:48px;font-family:var(--serif);font-weight:700;font-size:22px;letter-spacing:.5px;color:var(--ink)}
.main-nav{right:150px;top:54px;display:flex;align-items:center;font-size:13px;font-weight:500;letter-spacing:.3px}
.main-nav a{color:var(--ink);text-decoration:none;padding:0 16px;border-left:1px solid #bbb;line-height:14px}
.main-nav a:first-child{border-left:none;color:var(--gold)}
.search-btn{left:1104px;top:53px}

/* hero */
.hero{top:135px;height:611px}
.hero-photo{position:absolute;inset:0;background:linear-gradient(180deg,#c9c9c9 0%,#dedede 55%,#ececec 100%)}
.hero-copy{position:absolute;left:0;width:100%;top:154px;text-align:center}
.hero-copy .lead{font-weight:300;font-size:48px;line-height:60px;color:var(--ink)}
.hero-copy .big{font-weight:700;font-size:82px;line-height:96px;letter-spacing:1px}
.btn-dark{display:inline-block;background:var(--ink);color:var(--gold);font-size:14px;font-weight:500;letter-spacing:1px}
.hero .btn-dark{margin-top:14px;width:172px;height:43px;line-height:43px}
.dots{position:absolute;left:0;width:100%;display:flex;justify-content:center;gap:24px}
.dots span{width:13px;height:13px;border-radius:50%;background:var(--ink)}
.dots span.on{background:var(--paper);border:3px solid var(--ink)}

/* welcome */
.welcome{top:746px;height:689px}
.section-title{position:absolute;left:0;width:100%;text-align:center;font-size:32px;font-weight:300}
.section-title b{font-family:var(--serif);font-weight:700}
.section-title .gold{font-family:var(--serif);font-weight:400;color:var(--gold)}
.body-copy{font-size:13px;line-height:22px;color:var(--text)}
.intro{left:152px;top:172px;width:896px;text-align:center}
.col-title{font-size:22px;font-weight:400;margin-bottom:14px}
.col-title b{font-weight:700}
.col p+p{margin-top:18px}
.firm{left:150px;top:302px;width:404px}
.vision{left:655px;top:302px;width:395px}
.col-divider{left:603px;top:339px;width:1px;height:165px;background:var(--line)}
.welcome .btn-dark{position:absolute;left:534px;top:563px;width:132px;height:29px;line-height:29px;text-align:center;font-size:11px;color:var(--paper)}

/* practice */
.practice{top:1435px;height:546px;background:var(--mist)}
.areas{left:152px;top:205px;width:900px;display:grid;grid-template-columns:repeat(4,210px);column-gap:20px;row-gap:28px}
.area-head{display:flex;align-items:center;gap:14px;height:37px}
.area-icon{width:36px;height:36px;background:var(--ink);display:flex;align-items:center;justify-content:center;flex:none}
.area-name{font-size:14px;font-weight:500;line-height:16px}
.area p{margin-top:12px;font-size:11px;line-height:15px;color:var(--text)}

/* attorneys */
.attorneys{top:1981px;height:741px}
.attorneys .section-title{top:122px;font-size:32px}
.team{left:150px;top:230px;display:flex;gap:40px}
.member{width:278px}
.member-photo{height:249px;background:linear-gradient(180deg,#8d8d8d,#bdbdbd)}
.member-info{height:87px;background:#f1f1f1;text-align:center;padding-top:24px}
.member-name{font-size:15px;font-weight:500}
.member-role{font-size:12px;color:var(--text);margin-top:6px}

/* testimonials */
.testimonials{top:2722px;height:660px;background:var(--mist)}
.testimonials .section-title{top:72px;line-height:42px;font-size:32px}
.quotes{left:150px;top:204px;display:flex;gap:20px}
.quote-card{width:293px;height:312px;background:var(--paper);padding:0 28px;position:relative}
.avatar{width:70px;height:70px;border-radius:50%;background:linear-gradient(180deg,#a9a9a9,#d6d6d6);margin:25px auto 0}
.quote-mark{font-family:var(--serif);color:var(--gold);font-size:36px;font-weight:700;line-height:30px;margin-top:38px}
.quote-card p{font-size:12px;line-height:19px;color:var(--text);margin-top:6px}
.quote-author{font-size:14px;font-weight:500;margin-top:14px}

/* consultation */
.consult{top:3382px;height:546px}
.consult .section-title{top:96px;font-size:30px}
.field{position:absolute;width:396px}
.field label{display:block;font-size:13px;color:var(--text);margin-bottom:8px}
.field label sup{color:var(--ink);font-size:13px;top:0}
.input{height:37px;border:1px solid #d4d4d4;background:var(--paper)}
.textarea{height:135px;border:1px solid #d4d4d4}
.note{font-size:12px;color:var(--text)}
.agree{display:flex;align-items:center;gap:12px}
.check{width:15px;height:15px;border:1px solid #bdbdbd}

/* footer */
.site-footer{top:3928px;height:321px;background:linear-gradient(180deg,#e6e6e6,#eeeeee)}
.foot-title{font-size:18px;font-weight:400;letter-spacing:.5px;padding-bottom:10px;border-bottom:1px solid #c8c8c8;margin-bottom:16px}
.foot-brand{left:75px;top:80px;font-family:var(--serif);font-weight:700;font-size:22px}
.foot-about{left:75px;top:140px;width:240px;font-size:12px;line-height:18px;color:var(--text)}
.quick{left:396px;top:78px;width:140px}
.quick ul{list-style:none;font-size:12px;line-height:26px;color:#333}
.contact{left:617px;top:78px;width:200px}
.contact-line{display:flex;align-items:center;gap:8px;font-size:12px;line-height:20px;color:#333}
.follow{left:890px;top:78px;width:230px}
.social{display:flex;gap:18px;margin-top:4px}
.social span{width:14px;height:14px;border-radius:50%;background:var(--ink)}
.call-label{font-size:16px;letter-spacing:1px;margin-top:46px}
.call-number{font-size:24px;font-weight:700;letter-spacing:1px;margin-top:4px}
.bottom-bar{position:absolute;left:0;top:4249px;width:1200px;height:57px;background:var(--bar);color:#e5e5e5;font-size:13px;text-align:center;line-height:57px}
</style>
</head>
<body>

<header class="site-header">
  <div class="abs brand">LEGAL HAVEN</div>
  <nav class="abs main-nav">
    <a href="#">HOME</a><a href="#">ABOUT US</a><a href="#">OUR PEOPLE</a><a href="#">SERVICES</a><a href="#">CONTACT US</a>
  </nav>
  <svg class="abs search-btn" width="20" height="20" viewBox="0 0 20 20" aria-label="Search">
    <circle cx="10" cy="10" r="9" fill="none" stroke="#111" stroke-width="1.5"/>
    <circle cx="9" cy="9" r="3.5" fill="none" stroke="#111" stroke-width="1.5"/>
    <line x1="11.5" y1="11.5" x2="14" y2="14" stroke="#111" stroke-width="1.5"/>
  </svg>
</header>

<section class="hero">
  <div class="hero-photo" role="img" aria-label="Black and white photo of a smiling team of business professionals"></div>
  <div class="hero-copy">
    <div class="lead">Get your</div>
    <div class="lead">legal advice protect you &amp; your</div>
    <div class="big">BUSINESS</div>
    <span class="btn-dark">APPOINTMENT</span>
  </div>
  <div class="dots" style="top:545px"><span class="on"></span><span></span><span></span></div>
</section>

<section class="welcome">
  <h2 class="section-title" style="top:92px">Welcome To <b>LEGAL HAVEN</b></h2>
  <p class="abs body-copy intro">We are an independent legal practice offering clear, practical advice to families, individuals and small businesses. Our team listens first, explains your options in plain words and stays with you from the first meeting to the final outcome. Whether the matter is simple or complex, we treat it with the same care, discretion and attention to detail.</p>
  <div class="abs col firm">
    <h3 class="col-title">The <b>Firm</b></h3>
    <p class="body-copy">Founded on trust and experience, our firm has guided clients through disputes, agreements and life changes with honest, direct counsel.</p>
    <p class="body-copy">We keep fees transparent and explain every step, so you always know where your matter stands.</p>
  </div>
  <div class="abs col-divider"></div>
  <div class="abs col vision">
    <h3 class="col-title">Our <b>Vision</b></h3>
    <p class="body-copy">We aim to make good legal advice easy to reach, easy to understand and fairly priced for every client we serve.</p>
    <p class="body-copy">Our goal is lasting relationships built on results, respect and clear communication at every stage.</p>
  </div>
  <span class="btn-dark">READ MORE</span>
</section>

<section class="practice">
  <h2 class="section-title" style="top:80px">Our Legal <b>PRACTICE</b> <span class="gold">AREAS</span></h2>
  <div class="abs areas">
    <div class="area">
      <div class="area-head"><span class="area-icon"><svg width="22" height="22" viewBox="0 0 22 22"><circle cx="7" cy="6" r="3" fill="#fff"/><circle cx="15" cy="6" r="3" fill="#fff"/><path d="M2 19v-5a5 5 0 0 1 10 0v5zM10 19v-5a5 5 0 0 1 10 0v5z" fill="#fff"/></svg></span><span class="area-name">Family Law</span></div>
      <p>Separation, parenting and property matters handled with care, sensitivity and a focus on fair outcomes.</p>
    </div>
    <div class="area">
      <div class="area-head"><span class="area-icon"><svg width="22" height="22" viewBox="0 0 22 22"><circle cx="11" cy="7" r="4" fill="#fff"/><rect x="3" y="13" width="16" height="6" rx="1" fill="#fff"/></svg></span><span class="area-name">Debt Recovery</span></div>
      <p>Letters of demand, negotiation and court action to recover what is owed to your business.</p>
    </div>
    <div class="area">
      <div class="area-head"><span class="area-icon"><svg width="22" height="22" viewBox="0 0 22 22"><rect x="4" y="2" width="14" height="18" fill="none" stroke="#fff" stroke-width="2"/><line x1="7" y1="8" x2="15" y2="8" stroke="#fff" stroke-width="2"/><line x1="7" y1="12" x2="15" y2="12" stroke="#fff" stroke-width="2"/><line x1="7" y1="16" x2="12" y2="16" stroke="#fff" stroke-width="2"/></svg></span><span class="area-name">Leases</span></div>
      <p>Drafting, reviewing and negotiating commercial and retail leases so your terms are clear and secure.</p>
    </div>
    <div class="area">
      <div class="area-head"><span class="area-icon"><svg width="22" height="22" viewBox="0 0 22 22"><path d="M3 13l3-6h10l3 6v4H3z" fill="#fff"/><circle cx="7" cy="18" r="2" fill="#111" stroke="#fff" stroke-width="1.5"/><circle cx="15" cy="18" r="2" fill="#111" stroke="#fff" stroke-width="1.5"/></svg></span><span class="area-name">Crimes &amp; Traffic</span></div>
      <p>Advice and representation for criminal charges, licence matters and traffic offences in local courts.</p>
    </div>
    <div class="area">
      <div class="area-head"><span class="area-icon"><svg width="22" height="22" viewBox="0 0 22 22"><rect x="5" y="3" width="12" height="16" fill="#fff"/><line x1="8" y1="8" x2="14" y2="8" stroke="#111" stroke-width="1.5"/><line x1="8" y1="12" x2="14" y2="12" stroke="#111" stroke-width="1.5"/></svg></span><span class="area-name">Wills</span></div>
      <p>Simple and complex wills prepared to protect your family and carry out your wishes exactly.</p>
    </div>
    <div class="area">
      <div class="area-head"><span class="area-icon"><svg width="22" height="22" viewBox="0 0 22 22"><line x1="4" y1="4" x2="18" y2="18" stroke="#fff" stroke-width="3"/><line x1="18" y1="4" x2="4" y2="18" stroke="#fff" stroke-width="3"/></svg></span><span class="area-name">Violence<br>Restraining Orders</span></div>
      <p>Urgent help applying for or responding to restraining orders, with discreet and steady support.</p>
    </div>
    <div class="area">
      <div class="area-head"><span class="area-icon"><svg width="22" height="22" viewBox="0 0 22 22"><path d="M5 2h9l4 4v14H5z" fill="#fff"/><line x1="8" y1="10" x2="15" y2="10" stroke="#111" stroke-width="1.5"/><line x1="8" y1="14" x2="15" y2="14" stroke="#111" stroke-width="1.5"/></svg></span><span class="area-name">Probate Titles</span></div>
      <p>Guidance through probate, estate administration and the transfer of property titles to beneficiaries.</p>
    </div>
    <div class="area">
      <div class="area-head"><span class="area-icon"><svg width="22" height="22" viewBox="0 0 22 22"><path d="M14 3a8 8 0 1 0 5 13 6.5 6.5 0 1 1-5-13z" fill="#fff"/></svg></span><span class="area-name">Shariah Law</span></div>
      <p>Advice on Islamic wills, inheritance and family matters in line with Shariah principles and local law.</p>
    </div>
  </div>
</section>

<section class="attorneys">
  <h2 class="section-title"><b>OUR</b> <span class="gold">ATTORNEYS</span></h2>
  <div class="abs team">
    <div class="member"><div class="member-photo" role="img" aria-label="Portrait of a senior attorney in a suit"></div><div class="member-info"><div class="member-name">Marcus Hale</div><div class="member-role">Founder</div></div></div>
    <div class="member"><div class="member-photo" role="img" aria-label="Portrait of an attorney in an office library"></div><div class="member-info"><div class="member-name">Clara Whitmore</div><div class="member-role">CEO</div></div></div>
    <div class="member"><div class="member-photo" role="img" aria-label="Portrait of an attorney in a suit and tie"></div><div class="member-info"><div class="member-name">Owen Barrett</div><div class="member-role">Co Founder</div></div></div>
  </div>
  <div class="dots" style="top:630px"><span class="on"></span><span></span><span></span></div>
</section>

<section class="testimonials">
  <h2 class="section-title">See the <b>TESTIMONIALS</b><br>our clients have submitted so far</h2>
  <div class="abs quotes">
    <div class="quote-card">
      <div class="avatar" role="img" aria-label="Client portrait"></div>
      <div class="quote-mark">“</div>
      <p>Clear advice from the very first call. They explained every option and settled my matter quickly and fairly.</p>
      <div class="quote-author">- Nadia Fairlie</div>
    </div>
    <div class="quote-card">
      <div class="avatar" role="img" aria-label="Client portrait"></div>
      <div class="quote-mark">“</div>
      <p>Professional, patient and honest about costs. I always knew what was happening with my case.</p>
      <div class="quote-author">- Tom Brackett</div>
    </div>
    <div class="quote-card">
      <div class="avatar" role="img" aria-label="Client portrait"></div>
      <div class="quote-mark">“</div>
      <p>They recovered a debt I had given up on. Friendly team and real results for my business.</p>
      <div class="quote-author">- Henry Ashdown</div>
    </div>
  </div>
  <div class="dots" style="top:577px"><span class="on"></span><span></span><span></span></div>
</section>

<section class="consult">
  <h2 class="section-title">Request a <b>FREE</b> <span class="gold">CONSULTATION</span></h2>
  <div class="field" style="left:152px;top:196px"><label>Name <sup>*</sup></label><div class="input"></div></div>
  <div class="field" style="left:152px;top:279px"><label>Email <sup>*</sup></label><div class="input"></div></div>
  <div class="field" style="left:152px;top:365px"><label>Phone</label><div class="input"></div></div>
  <div class="field" style="left:675px;top:196px"><label>Description</label><div class="textarea"></div></div>
  <div class="abs note" style="left:675px;top:363px">* Required</div>
  <div class="abs agree note" style="left:675px;top:402px"><span class="check"></span>I have read the Disclaimer and Privacy Policy</div>
</section>

<footer class="site-footer">
  <div class="abs foot-brand">LEGAL HAVEN</div>
  <p class="abs foot-about">Independent legal advice for families and businesses, delivered with care and plain speaking.</p>
  <div class="abs quick">
    <h4 class="foot-title">QUICK LINKS</h4>
    <ul><li>Home</li><li>About Us</li><li>Our people</li><li>Services</li><li>Contact Us</li></ul>
  </div>
  <div class="abs contact">
    <h4 class="foot-title">CONTACT</h4>
    <div class="contact-line" style="line-height:18px">240 Alder Row<br>Brookfield, ST 00421</div>
    <div class="contact-line" style="margin-top:8px"><svg width="12" height="12" viewBox="0 0 12 12"><path d="M2 1h3l1 3-2 1a7 7 0 0 0 3 3l1-2 3 1v3a1 1 0 0 1-1 1A10 10 0 0 1 1 2a1 1 0 0 1 1-1z" fill="#111"/></svg>555-014-2288</div>
    <div class="contact-line"><svg width="12" height="12" viewBox="0 0 12 12"><rect x="3" y="0" width="6" height="12" rx="1" fill="#111"/></svg>555-014-7731</div>
    <div class="contact-line"><svg width="12" height="12" viewBox="0 0 12 12"><rect x="0" y="2" width="12" height="8" fill="#111"/><path d="M0 2l6 5 6-5" fill="none" stroke="#fff"/></svg>contact@legalhaven.example</div>
    <div class="contact-line"><svg width="12" height="12" viewBox="0 0 12 12"><circle cx="6" cy="6" r="5.5" fill="#111"/></svg>www.legalhaven.example</div>
  </div>
  <div class="abs follow">
    <h4 class="foot-title">FOLLOW US ON</h4>
    <div class="social"><span></span><span></span><span></span><span></span></div>
    <div class="call-label">CALL US ON</div>
    <div class="call-number">555-014-2288</div>
  </div>
</footer>
<div class="bottom-bar">© 2017 legalhaven &nbsp;|&nbsp; Privacy Policy &nbsp;|&nbsp; User Agreement</div>

</body>
</html>
```